New Brochure Design Project

We need a fresh, professional and modern brochure design template that we can use to communicate our products and services to our customers.
The Brochure has to fit to our corporate style which can be found at: www.brovalto.nl
Our products can be found at: www.shop.brovalto.nl

The brochure has to be in A-4 format and has to contain:
- one front
- two different content pages (tekst and photo's)
- one back

Goodluck,

Team Brovalto.

```html
<!DOCTYPE html>
<html lang="en">
<head>
<meta charset="utf-8">
<title>Brovalto Brochure</title>
<link rel="stylesheet" href="https://fonts.googleapis.com/css2?family=Montserrat:wght@300;400;600;700&display=swap">
<style>
  :root {
    --orange: #f7941d;
    --orange-deep: #f07f12;
    --orange-light: #fbb03b;
    --heading-grey: #8c8f93;
    --body-grey: #a3a5a8;
    --white: #ffffff;
    --dark: #1a1a1a;
    --dark-top: #3d3d3d;
  }
  * { box-sizing: border-box; margin: 0; padding: 0; }
  html, body { width: 1200px; height: 853px; overflow: hidden; background: var(--white); }
  body { position: relative; font-family: "Montserrat", sans-serif; }

  .hero-panel {
    position: absolute; left: 12px; top: 10px; width: 565px; height: 247px;
    display: flex; box-shadow: 0 8px 8px -6px rgba(0,0,0,.25);
  }
  .hero-panel__text {
    width: 276px; height: 100%;
    background: linear-gradient(135deg, var(--orange-light) 0%, var(--orange) 45%, var(--orange-deep) 100%);
    padding: 56px 16px 0 18px; color: var(--white);
  }
  .hero-panel__photo {
    flex: 1; background: linear-gradient(120deg, #e9edf1 0%, #cfd8e2 45%, #9fb1c6 70%, #5a6470 100%);
  }
  .panel-title { font-size: 20px; font-weight: 700; color: var(--white); line-height: 24px; }
  .panel-copy {
    font-size: 11px; font-weight: 400; line-height: 12.4px; text-align: justify; color: var(--white);
  }

  .services { position: absolute; left: 62px; top: 308px; width: 474px; }
  .service { position: absolute; left: 0; width: 474px; display: flex; }
  .service__icon { width: 64px; height: 64px; flex: none; margin-right: 16px; margin-top: 26px; }
  .service__icon svg { width: 64px; height: 64px; fill: var(--orange); }
  .service__body { width: 394px; }
  .service__title { font-size: 20px; font-weight: 700; color: var(--heading-grey); line-height: 24px; }
  .service__copy {
    font-size: 11px; font-weight: 300; line-height: 12.4px; color: var(--body-grey); text-align: justify;
  }
  .service__copy + .service__copy { margin-top: 12px; }

  .intro-panel {
    position: absolute; left: 611px; top: 10px; width: 562px; height: 298px;
    background: linear-gradient(140deg, var(--orange-light) 0%, var(--orange) 40%, var(--orange-deep) 100%);
    padding: 48px 20px 0 31px;
  }
  .intro-panel::after {
    content: ""; position: absolute; left: 267px; bottom: -14px;
    border-left: 14px solid transparent; border-right: 14px solid transparent;
    border-top: 14px solid var(--orange-deep);
  }
  .intro-panel .panel-copy + .panel-copy { margin-top: 18px; }

  .features { position: absolute; top: 334px; left: 622px; width: 550px; }
  .feature { position: absolute; top: 0; width: 165px; }
  .feature__title { font-size: 20px; font-weight: 700; color: var(--heading-grey); line-height: 24px; }
  .feature__photo { width: 165px; height: 103px; margin-top: 4px; }
  .feature__copy {
    margin-top: 17px; font-size: 11px; font-weight: 300; line-height: 12.4px;
    color: var(--body-grey); text-align: justify;
  }
  .photo-touch { background: linear-gradient(135deg, #0e5d8c 0%, #3a9ad0 50%, #cfe6f4 100%); }
  .photo-desk { background: linear-gradient(135deg, #f1f1ef 0%, #d9d3cc 45%, #7a6a5c 100%); }
  .photo-network { background: linear-gradient(135deg, #d8e8f4 0%, #a9c4dc 50%, #d95b5b 100%); }

  .back-cover {
    position: absolute; left: 701px; top: 672px; width: 376px; height: 181px;
    border-radius: 12px 12px 0 0;
    background: linear-gradient(180deg, var(--dark-top) 0%, #222 55%, var(--dark) 100%);
    display: flex; align-items: center; justify-content: center; gap: 16px; padding-bottom: 20px;
  }
  .brand-dot { width: 44px; height: 44px; border-radius: 50%; background: var(--orange); }
  .brand-name { font-size: 44px; font-weight: 400; color: #b5b7ba; letter-spacing: 0.5px; }
</style>
</head>
<body>

  <section class="hero-panel">
    <div class="hero-panel__text">
      <h2 class="panel-title">Lorem ipsum</h2>
      <p class="panel-copy">Lorem ipsum dolor sit amet, consectetur adipiscing elit. Cras sodales, enim ac porta sagittis, orci nunc rhoncus justo, sit amet consequat ipsum magna at nulla. Nulla placerat lorem nec magna adipiscing, nec tincidunt nulla vulputate. Mauris eleifend augue at purus commodo, eget interdum mauris sagittis</p>
    </div>
    <div class="hero-panel__photo" role="img" aria-label="Photo of a smiling businessman working at a laptop in a bright office"></div>
  </section>

  <section class="services">
    <article class="service" style="top:0">
      <div class="service__icon">
        <svg viewBox="0 0 64 64" aria-hidden="true"><path d="M27 4h10l2 8 6 3 7-4 7 7-4 7 3 6 8 2v10l-8 2-3 6 4 7-7 7-7-4-6 3-2 8H27l-2-8-6-3-7 4-7-7 4-7-3-6-8-2V27l8-2 3-6-4-7 7-7 7 4 6-3zM32 20a12 12 0 1 0 0 24 12 12 0 1 0 0-24z" fill-rule="evenodd"/></svg>
      </div>
      <div class="service__body">
        <h3 class="service__title">Agile Software Development</h3>
        <p class="service__copy">Brovalto develops high-standard Custom applications, Mercato Webshops/Modules and Professional websites that perform! We can integrate every platform that provides an API.</p>
        <p class="service__copy">We use Agile projectmanagement techniques like Scrum and Extreme Programming to deliver the best possible quality and help you to get your Return on Investment as soon as possible.</p>
      </div>
    </article>

    <article class="service" style="top:135px">
      <div class="service__icon" style="margin-top:-2px">
        <svg viewBox="0 0 64 64" aria-hidden="true"><path d="M8 18h14a7 7 0 1 1 12 0h14v14a7 7 0 1 1 0 12v14H34a7 7 0 1 0-12 0H8V44a7 7 0 1 0 0-12z" transform="rotate(-20 32 36)"/></svg>
      </div>
      <div class="service__body">
        <h3 class="service__title">Mercato Module Development</h3>
        <p class="service__copy">With our decade of experience in Mercato Webshops, we know exactly what kind of Mercato modules your webshop needs. If a desired Mercato Module doesn't exist yet, we can create this module for you!</p>
      </div>
    </article>

    <article class="service" style="top:225px">
      <div class="service__icon" style="margin-top:0">
        <svg viewBox="0 0 64 64" aria-hidden="true"><path d="M24 8h16a3 3 0 0 1 3 3v5h13a4 4 0 0 1 4 4v34a4 4 0 0 1-4 4H8a4 4 0 0 1-4-4V20a4 4 0 0 1 4-4h13v-5a3 3 0 0 1 3-3zm1 4v4h14v-4z" fill-rule="evenodd"/></svg>
      </div>
      <div class="service__body">
        <h3 class="service__title">Portfolio</h3>
        <p class="service__copy">Thanks to our experience with Agile Software Development, Mercato Webshops and High-Performance websites, Brovalto can deliver you a incredible quality while the costs are kept as low as possible. Check our Portfolio to see what we've done so far!</p>
      </div>
    </article>

    <article class="service" style="top:307px">
      <div class="service__icon" style="margin-top:4px">
        <svg viewBox="0 0 64 64" aria-hidden="true"><circle cx="32" cy="32" r="31"/><circle cx="32" cy="17" r="5" fill="#fff"/><path d="M26 26h10v20h4v5H24v-5h4V31h-2z" fill="#fff"/></svg>
      </div>
      <div class="service__body">
        <h3 class="service__title">About us</h3>
        <p class="service__copy">With Agile Software Development, you're assured of maximum return of investment with minimal overhead. Thanks to a potentially shipable increment every sprint, the risk is reducing during the project time period. We're always using the most optimal techniques available to the team, instead of holding on to what we knew 5 years ago.</p>
      </div>
    </article>

    <article class="service" style="top:421px">
      <div class="service__icon" style="margin-top:-6px">
        <svg viewBox="0 0 64 64" aria-hidden="true"><path d="M10 6l6 2 30 30 4-2 10 10a6 6 0 0 1-12 12L38 48l2-4L10 14l-4-2z"/><path d="M44 4a12 12 0 0 0-10 16L6 48a5 5 0 0 0 8 8l28-28a12 12 0 0 0 16-10l-7 4-6-2-2-6 7-5a12 12 0 0 0-6-5z"/></svg>
      </div>
      <div class="service__body">
        <h3 class="service__title">Support</h3>
        <p class="service__copy">Brovalto offers interactive, personal support on all our services and products. We uphold a transparant and customer friendly service as thats what we value the most.</p>
      </div>
    </article>
  </section>

  <section class="intro-panel">
    <h2 class="panel-title">Lorem ipsum</h2>
    <p class="panel-copy">Lorem ipsum dolor sit amet, consectetur adipiscing elit. Cras sodales, enim ac porta sagittis, orci nunc rhoncus justo, sit amet consequat ipsum magna at nulla. Nulla placerat lorem nec magna adipiscing, nec tincidunt nulla vulputate. Mauris eleifend augue at purus commodo, eget interdum mauris sagittis</p>
    <p class="panel-copy">In malesuada augue sed odio bibendum, quis adipiscing est cursus. Sed in rhoncus nulla. Nunc tincidunt quam eget ornare posuere. Integer ornare, orci vitae varius mattis, neque nisl ornare diam, imperdiet ultrices enim lectus eget mauris. Nullam aliquet adipiscing augue, a iaculis erat iaculis convallis. Vestibulum a nisi nec nisi vehicula gravida ut sodales tellus. Nam auctor vitae erat et adipiscing. In elementum est eget iaculis egestas. Nulla sit amet vulputate lacus. Nulla sapien lorem, iaculis eu erat eget, luctus euismod est. In turpis neque, laoreet vel suscipit a, accumsan sed tortor. Sed tempor ipsum et rhoncus mattis. Nunc molestie dictum elit, quis vestibulum nulla. Morbi at purus eget dolor condimentum facilisis.</p>
  </section>

  <section class="features">
    <article class="feature" style="left:0">
      <h3 class="feature__title">Lorem ipsum</h3>
      <div class="feature__photo photo-touch" role="img" aria-label="Photo of a finger touching a blue touchscreen"></div>
      <p class="feature__copy">Lorem ipsum dolor sit amet, consectetur adipiscing elit. Cras sodales, enim ac porta sagittis, orci nunc rhoncus justo, sit amet consequat ipsum magna at nulla. Nulla placerat lorem nec magna adipiscing, nec tincidunt nulla vulputate. Mauris eleifend augue at purus commodo, eget interdum mauris sagittis</p>
    </article>
    <article class="feature" style="left:197px">
      <h3 class="feature__title">Lorem ipsum</h3>
      <div class="feature__photo photo-desk" role="img" aria-label="Photo of a woman working at a desktop computer"></div>
      <p class="feature__copy">Lorem ipsum dolor sit amet, consectetur adipiscing elit. Cras sodales, enim ac porta sagittis, orci nunc rhoncus justo, sit amet consequat ipsum magna at nulla. Nulla placerat lorem nec magna adipiscing, nec tincidunt nulla vulputate. Mauris eleifend augue at purus commodo, eget interdum mauris sagittis</p>
    </article>
    <article class="feature" style="left:386px">
      <h3 class="feature__title">Lorem ipsum</h3>
      <div class="feature__photo photo-network" role="img" aria-label="Photo of network cables plugged into a server switch"></div>
      <p class="feature__copy">Lorem ipsum dolor sit amet, consectetur adipiscing elit. Cras sodales, enim ac porta sagittis, orci nunc rhoncus justo, sit amet consequat ipsum magna at nulla. Nulla placerat lorem nec magna adipiscing, nec tincidunt nulla vulputate. Mauris eleifend augue at purus commodo, eget interdum mauris sagittis</p>
    </article>
  </section>

  <section class="back-cover">
    <span class="brand-dot" aria-hidden="true"></span>
    <span class="brand-name">Brovalto</span>
  </section>

</body>
</html>
```